Etikett für Kreativbier Morgenglut
Sehr schönes und professionelles Design - gerne wieder :-)
Zielgruppe
Wir sind eine kleine Brauerei und möchten gemeinsam mit einem Weingut ein Kreativbier 'Morgenglut' produzieren.
Aufgabenstellung
Da das Kreativbier eine Mischung aus Bier und Wein zweier unterschiedlicher Betriebe ist, sollen beim Etikett auch beide Firmenlogos miteinander 'verheiratet' werden. Als Platzbedarf für die Grafik stehen 117x55mm zur Verfügung. Auch die Bezeichnung 'Morgenglut' sollte in die Grafik mit eingearbeitet werden.

```html
<!DOCTYPE html>
<html lang="de">
<head>
<meta charset="utf-8">
<title>Morgenglut – Etikett</title>
<link rel="stylesheet" href="https://fonts.googleapis.com/css2?family=Italiana&family=Playfair+Display:wght@700&display=swap">
<style>
  :root {
    --canvas: #d6cfcb;
    --label: #ffffff;
    --wine-red: #a82410;
    --beer-beige: #b39470;
    --grape-rose: #d49a92;
    --ampersand-faint: #ece3d9;
    --partner-gold: #bfa062;
    --divider: #c0574a;
  }
  * { margin: 0; padding: 0; box-sizing: border-box; }
  html, body {
    width: 1200px;
    height: 2400px;
    overflow: hidden;
    background: var(--canvas);
  }
  .label {
    position: absolute;
    left: 115px;
    top: 617px;
    width: 970px;
    height: 456px;
    background: var(--label);
    overflow: hidden;
  }
  .label > * { position: absolute; }

  .ampersand-faint {
    left: 20px;
    top: 60px;
    font-family: "Playfair Display", serif;
    font-weight: 700;
    font-size: 340px;
    line-height: 1;
    color: var(--ampersand-faint);
  }
  .art-wheat {
    left: 45px; top: 138px; width: 105px; height: 275px;
    background: linear-gradient(170deg, #ddc9ad, #cdb495);
    border-radius: 50% 50% 20% 20%;
    opacity: .85;
  }
  .art-grapes {
    left: 104px; top: 54px; width: 136px; height: 215px;
    background: linear-gradient(180deg, #e6bdb6, #dca59d);
    border-radius: 45% 45% 50% 50% / 35% 35% 65% 65%;
  }
  .art-glass {
    left: 450px; top: 31px; width: 30px; height: 48px;
    background: var(--grape-rose);
    border-radius: 40% 40% 20% 20%;
  }
  .art-hop {
    left: 470px; top: 324px; width: 82px; height: 68px;
    background: linear-gradient(160deg, #c9ae88, #b39470);
    border-radius: 45%;
  }
  .art-leaf {
    left: 788px; top: 275px; width: 160px; height: 160px;
    background: linear-gradient(150deg, #f0d6d2, #e2b2ab);
    border-radius: 48% 52% 46% 54%;
  }

  .product-name {
    left: 250px;
    font-family: "Italiana", serif;
    line-height: 1;
    white-space: nowrap;
  }
  .product-name--top { top: 88px; font-size: 96px; color: var(--wine-red); letter-spacing: 0; }
  .product-name--bottom { top: 185px; font-size: 150px; color: var(--beer-beige); letter-spacing: 6px; }

  .divider {
    left: 648px; top: 20px; width: 4px; height: 405px;
    background: var(--divider);
  }

  .partner {
    font-family: "Italiana", serif;
    color: var(--partner-gold);
    white-space: nowrap;
    text-align: center;
    line-height: 1;
  }
  .partner--winery {
    left: 680px; top: 96px; width: 140px;
    font-size: 22px; letter-spacing: 1px;
  }
  .partner-rule {
    left: 700px; top: 126px; width: 100px; height: 3px;
    background: var(--partner-gold);
  }
  .partner-mark {
    left: 732px; top: 150px; width: 38px; height: 38px;
    border-radius: 50%;
    background: var(--partner-gold);
  }
  .partner--brewery {
    left: 680px; top: 210px; width: 140px;
    font-size: 16px; letter-spacing: 1px;
  }

  .ampersand-bold {
    left: 826px; top: 71px;
    font-family: "Playfair Display", serif;
    font-weight: 700;
    font-size: 138px;
    line-height: 1;
    color: var(--wine-red);
  }
</style>
</head>
<body>
  <main class="label" aria-label="Etikett Morgenglut">
    <div class="ampersand-faint" aria-hidden="true">&amp;</div>
    <div class="art-wheat" role="img" aria-label="Illustration einer Weizenähre"></div>
    <div class="art-grapes" role="img" aria-label="Illustration einer Weintraube"></div>
    <div class="art-glass" role="img" aria-label="Kleines Weinglas-Symbol"></div>

    <h1 class="product-name product-name--top">MORGEN</h1>
    <p class="product-name product-name--bottom">GLUT</p>

    <div class="art-hop" role="img" aria-label="Illustration einer Hopfendolde"></div>

    <div class="divider" aria-hidden="true"></div>

    <p class="partner partner--winery">HALLREITER</p>
    <div class="partner-rule" aria-hidden="true"></div>
    <div class="partner-mark" aria-hidden="true"></div>
    <p class="partner partner--brewery">TALBACH BRÄU</p>

    <div class="ampersand-bold" aria-hidden="true">&amp;</div>

    <div class="art-leaf" role="img" aria-label="Illustration eines Weinblatts"></div>
  </main>
</body>
</html>
```